Business Card Design Project

I am a new business offering a consulting service in Homeware buying, product development and trend forecasting. I would like to use colours that are current and on trend now. Needs to be eye catching, speak of creativity and design.

Front: Matt charcoal card with black gloss embossing name print
Back: white with Pink text

Pink pantone: 812c

Target Market(s)

Retailers and Wholesalers of Homeware products

Industry/Entity Type

Business

Requirements
Must have
• Please go to this link and the card on this link is what I am looking for.

http://www.foliorama.net/gallery/Blank_sheet-KX/402817

1. Card Front

Name on front of card: MARGOT FINCHLEY

2. Back card

The following text must be designed onto the card:

Address: 17 Walloway Street ,Paddington, 2021, NSW, Sydney, Australia
Mobile: +61 (0)412305718
Email: finchmel@wirrolink.net.au

Homeware trends
Product development and sourcing
Strategic Buying management
Nice to have
• Creativity in selection of font, composition and proportion.
Should not have
• I don't want to see graphics/shapes on the card.

```html
<!DOCTYPE html>
<html lang="en">
<head>
<meta charset="utf-8">
<title>Margot Finchley – Business Card</title>
<link rel="stylesheet" href="https://fonts.googleapis.com/css2?family=Jost:wght@400&display=swap">
<style>
  :root {
    --backdrop: #8a8a86;
    --card-white: #f4f5f6;
    --card-charcoal: #29323a;
    --pantone-pink: #d8478a;
  }
  * { box-sizing: border-box; margin: 0; padding: 0; }
  html, body {
    width: 1200px;
    height: 792px;
    overflow: hidden;
  }
  body {
    background: var(--backdrop);
    font-family: "Jost", "Futura", sans-serif;
  }
  .card-spread {
    position: absolute;
    top: 231px;
    left: 40px;
    display: flex;
    gap: 40px;
  }
  .card {
    width: 540px;
    height: 330px;
    position: relative;
    box-shadow: 0 6px 18px rgba(0, 0, 0, 0.25);
  }

  /* Back of card: white with pink text */
  .card-back {
    background: var(--card-white);
    color: var(--pantone-pink);
    padding: 112px 0 0 58px;
  }
  .services {
    list-style: none;
    font-size: 18px;
    line-height: 23px;
    margin-bottom: 20px;
  }
  .contact-list {
    list-style: none;
    font-size: 18px;
    line-height: 23px;
  }
  .contact-item {
    display: flex;
    align-items: flex-start;
    gap: 12px;
  }
  .contact-icon {
    width: 15px;
    height: 15px;
    flex: none;
    margin-top: 4px;
    fill: var(--pantone-pink);
  }

  /* Front of card: matt charcoal with the name set as plain type */
  .card-front {
    background: var(--card-charcoal);
    display: flex;
    align-items: center;
    justify-content: center;
  }
  .card-name {
    font-size: 30px;
    font-weight: 400;
    letter-spacing: 8px;
    text-transform: uppercase;
    color: var(--pantone-pink);
  }
</style>
</head>
<body>
  <main class="card-spread">
    <section class="card card-back" aria-label="Card back">
      <ul class="services">
        <li>Homeware trends</li>
        <li>Product development and sourcing</li>
        <li>Strategic Buying management</li>
      </ul>
      <ul class="contact-list">
        <li class="contact-item">
          <svg class="contact-icon" viewBox="0 0 16 16" aria-hidden="true">
            <path d="M8 1 L15.5 8 H13 V15 H9.5 V10.5 H6.5 V15 H3 V8 H0.5 Z"/>
          </svg>
          <span>17 Walloway Street, Paddington, 2021<br>NSW, Sydney, Australia</span>
        </li>
        <li class="contact-item">
          <svg class="contact-icon" viewBox="0 0 16 16" aria-hidden="true">
            <path d="M3.5 1 L6 1 L7 5 L5.2 6.3 C6 8.2 7.8 10 9.7 10.8 L11 9 L15 10 L15 12.5 C15 14 14 15 12.5 15 C6.8 15 1 9.2 1 3.5 C1 2 2 1 3.5 1 Z"/>
          </svg>
          <span>+61 (0)412305718</span>
        </li>
        <li class="contact-item">
          <svg class="contact-icon" viewBox="0 0 16 16" aria-hidden="true">
            <path d="M1 3 H15 V13 H1 Z M2.5 4.5 L8 9 L13.5 4.5 Z" fill-rule="evenodd"/>
          </svg>
          <span>finchmel@wirrolink.net.au</span>
        </li>
      </ul>
    </section>

    <section class="card card-front" aria-label="Card front">
      <h1 class="card-name">Margot Finchley</h1>
    </section>
  </main>
</body>
</html>
```